Webdesign für Freelancer Web/App (OnePager)
Zielgruppe
Ich bin ein Freelancer im Bereich Web- und App-Entwicklung. Über eine professionelle Webseite möchte ich neue Kunden gewinnen. Dazu möchte ich mich und meine Leistungen vorstellen und dem Benutzer die Möglichkeit bieten meine Arbeiten anzuschauen und mich zu kontaktieren.
Aufgabenstellung
Optisch gefallen mir Onepager sehr gut (z.B. http://muster.veltora.com/). Ich möchte mir aber offen halten, auch mehrere Unterseiten zu erstellen. Inhaltlich kann man sich bspw. an https://www.quintelor.ch/ orientieren.
Es geht ausschliesslich um die Umsetzung des Webdesigns.
Es sind bereits ein Logo, eine Schrift und 2 Farben definiert. Nur das Blau muss verwendet werden, das grün ist optional. Weitere Farben und 1 weitere Schrift dürfen verwendet werden. Das Logo darf mit oder ohne Schriftzug verwendet werden. Freie Stock-Fotos dürfen verwendet werden. Das Design muss auf Desktop (optimiert auf ca. 1400px) und Mobile funktionieren (Responsive). Nice to have wären optimierte App- und Favicons die auch vom Logo abweichen dürfen. Nice to have wäre ein Fendora Map Pin.

```html
<!DOCTYPE html>
<html lang="de">
<head>
<meta charset="utf-8">
<title>MASO – Marek Solin, Web Entwickler</title>
<link href="https://fonts.googleapis.com/css2?family=Quicksand:wght@400;500;600;700&display=swap" rel="stylesheet">
<style>
:root{
  --navy:#12335a;
  --navy-deep:#0d2a4c;
  --green:#36cc96;
  --ink:#1d2d44;
  --muted:#6f7b8a;
  --light:#f4f7fb;
  --line:#e3e8ef;
  --white:#ffffff;
}
*{box-sizing:border-box;margin:0;padding:0}
html,body{width:1200px;height:2962px;overflow:hidden}
body{position:relative;font-family:"Quicksand",sans-serif;color:var(--ink);background:var(--white)}
.abs{position:absolute}
a{color:inherit;text-decoration:none}

/* hero */
.hero{left:0;top:0;width:1200px;height:537px;background:linear-gradient(180deg,#143a66 0%,#12335a 45%,#1a3e66 75%,#12335a 100%)}
.brand{left:236px;top:36px;display:flex;align-items:center;gap:10px}
.brand-mark{width:12px;height:12px;background:var(--green)}
.brand-name{font-size:24px;line-height:30px;font-weight:600;color:var(--white);letter-spacing:1px}
.nav{top:45px;left:712px;display:flex;gap:16px;font-size:10.5px;font-weight:700;color:var(--white);letter-spacing:.2px}
.nav a.active{color:var(--green);border-bottom:1px solid var(--green);padding-bottom:2px}
.hero-title{left:291px;top:280px;font-size:28px;line-height:33px;color:var(--white);font-weight:400}
.hero-title b{font-weight:600}
.hero-title .accent{color:var(--green)}
.hero-sub{left:291px;top:354px;font-size:13px;color:var(--white);font-weight:500}

/* intro band */
.band{left:0;top:537px;width:1200px;height:258px;background:var(--green)}
.pillar{top:590px;width:214px;text-align:center;color:var(--white)}
.pillar svg{display:block;margin:0 auto 14px}
.pillar h3{font-size:13px;font-weight:500;margin-bottom:12px}
.pillar p{font-size:9px;line-height:14px;opacity:.92}
.avatar{left:547px;top:749px;width:102px;height:102px;border-radius:50%;border:4px solid var(--white);background:radial-gradient(circle at 50% 40%,#e2b79c 0%,#b88a73 40%,#56616d 75%,#d9dde2 100%);box-shadow:0 4px 12px rgba(0,0,0,.15)}
.quote-mark{left:0;width:1200px;top:878px;text-align:center;font-size:22px;font-weight:600;color:var(--navy)}
.statement{left:355px;width:490px;top:913px;text-align:center;font-size:13px;line-height:17.5px;color:var(--ink)}
.statement b{font-weight:700;color:var(--navy)}
.statement u{text-underline-offset:2px}

/* services */
.services{left:0;top:1032px;width:1200px;height:666px;background:var(--light)}
.section-title{left:0;width:1200px;text-align:center;font-size:17px;font-weight:500;color:var(--ink)}
.section-title span{color:var(--green)}
.section-sub{left:0;width:1200px;text-align:center;font-size:10.5px;color:var(--muted)}
.card{width:356px;height:127px;background:var(--white);border:1px solid var(--line)}
.card.active{border:2px solid var(--navy);box-shadow:0 4px 14px rgba(18,51,90,.12)}
.card svg,.card .icon-t{position:absolute;left:24px;top:26px}
.card h4{position:absolute;left:82px;top:22px;font-size:12.5px;font-weight:500;color:var(--ink)}
.card p{position:absolute;left:82px;top:52px;width:248px;font-size:9px;line-height:14px;color:var(--muted)}
.icon-t{font-family:Georgia,serif;font-weight:700;font-size:42px;line-height:40px;color:var(--navy)}
.btn{background:var(--green);color:var(--white);font-size:9.5px;font-weight:700;text-align:center;border-radius:2px;letter-spacing:.3px}

/* references */
.divider{left:426px;top:1795px;width:345px;height:1px;background:var(--line)}
.filters{top:1806px;left:460px;display:flex;gap:26px;font-size:10.5px;color:var(--muted)}
.filters .on{color:var(--green);text-decoration:underline;text-underline-offset:3px;font-weight:600}
.tile{overflow:hidden}
.yacht{background:rgba(18,51,90,.93);color:var(--white);text-align:center;padding-top:30px}
.yacht small{display:block;font-size:9.5px}
.yacht strong{display:block;font-size:14px;font-weight:700;margin:6px 0 6px}
.yacht span{display:block;font-size:9.5px;line-height:11px;padding:0 28px}
.yacht em{display:block;font-size:9.5px;color:var(--green);text-decoration:underline;margin-top:8px}

/* contact */
.footer{left:0;top:2462px;width:1200px;height:500px;background:linear-gradient(180deg,#143761 0%,#12335a 40%,#113258 100%)}
.stripe{left:0;top:2946px;width:1200px;height:16px;background:var(--green)}
.form-card{left:368px;top:2363px;width:459px;height:320px;background:var(--white);border:3px solid var(--navy);box-shadow:0 10px 30px rgba(0,0,0,.12)}
.form-card h3{position:absolute;left:28px;top:30px;font-size:13.5px;font-weight:500;color:var(--ink)}
.field{position:absolute;border-bottom:1px solid var(--line);height:32px}
.field label{display:block;font-size:7.5px;color:var(--muted)}
.field span{display:block;font-size:9.5px;margin-top:7px;color:var(--ink);white-space:nowrap}
.foot-text{font-size:9.5px;line-height:15px;color:var(--white)}
.foot-list{font-size:9.5px;line-height:19.5px;color:var(--white);list-style:none}
</style>
</head>
<body>

<!-- hero -->
<div class="abs hero" role="img" aria-label="Stadtansicht von St. Gallen mit blauer Farbüberlagerung"></div>
<div class="abs brand"><span class="brand-mark"></span><span class="brand-name">MASO</span></div>
<nav class="abs nav">
  <a href="#">ÜBER MICH</a><a href="#">LEISTUNGEN</a><a href="#">REFERENZEN</a><a href="#" class="active">KONTAKT</a>
</nav>
<h1 class="abs hero-title">Ich bin <b>Ma</b>rek <b>So</b>lin,<br><span class="accent">Web Entwickler_</span> aus St. Gallen</h1>
<p class="abs hero-sub">Praesent egestas tristique nibh. Sed a libero. Cras varius. Donec vitae orci sed dolor.</p>

<!-- intro -->
<section class="abs band"></section>
<div class="abs pillar" style="left:247px">
  <svg width="24" height="24" viewBox="0 0 24 24" fill="none" stroke="#fff" stroke-width="1.8"><path d="M9 3a9 9 0 1 0 12 12A8 8 0 0 1 9 3z"/></svg>
  <h3>Über mich</h3>
  <p>Suspendisse potenti. Pellentesque commodo eros a enim. Vestibulum turpis sem, aliquet eget, lobortis pellentesque, rutrum eu, nisl. Sed libero. Aliquam erat volutpat.</p>
</div>
<div class="abs pillar" style="left:491px">
  <svg width="24" height="24" viewBox="0 0 24 24" fill="none" stroke="#fff" stroke-width="1.8"><path d="M12 3l9 9-9 9-9-9z"/></svg>
  <h3>Meine Erfahrung</h3>
  <p>Suspendisse potenti. Pellentesque commodo eros a enim. Vestibulum turpis sem, aliquet eget, lobortis pellentesque, rutrum eu, nisl. Sed libero. Aliquam erat volutpat.</p>
</div>
<div class="abs pillar" style="left:735px">
  <svg width="24" height="24" viewBox="0 0 24 24" fill="none" stroke="#fff" stroke-width="1.8"><path d="M12 3l10 18H2z"/></svg>
  <h3>Meine Vision</h3>
  <p>Suspendisse potenti. Pellentesque commodo eros a enim. Vestibulum turpis sem, aliquet eget, lobortis pellentesque, rutrum eu, nisl. Sed libero. Aliquam erat volutpat.</p>
</div>
<div class="abs avatar" role="img" aria-label="Porträtfoto von Marek Solin"></div>
<div class="abs quote-mark">“</div>
<p class="abs statement">Ich plane, gestalte und realisiere <b>erfolgreiche Webprojekte</b> für Ihr Unterneh-<br>men. <u>Als Full-Service-Provider</u> biete ich Ihnen alles Erforderliche, um im Internet<br>erfolgreich und professionell aufzutreten.</p>

<!-- services -->
<section class="abs services"></section>
<h2 class="abs section-title" style="top:1071px">Meine Leistungen<span>_</span></h2>
<p class="abs section-sub" style="top:1096px">Mein Leistungsspektrum umfasst folgende Tätigkeiten:</p>

<div class="abs card" style="left:235px;top:1160px">
  <svg width="34" height="34" viewBox="0 0 34 34" fill="none" stroke="#12335a" stroke-width="1.5"><path d="M12 18a6 6 0 1 1 10 0c-1.5 1.5-2 2.5-2 4h-6c0-1.5-.5-2.5-2-4z"/><path d="M14 25h6M15 28h4M17 4v3M6 12h3M25 12h3M9 6l2 2M25 6l-2 2"/></svg>
  <h4>Ideen, Beratung &amp; Konzept</h4>
  <p>Eine kompetente und detaillierte Planung Ihres Projektes beziehungsweise Webauftritts steht für uns an erster Stelle und ist ein unerlässlicher Dienstleistungsbestandteil.</p>
</div>
<div class="abs card" style="left:609px;top:1160px">
  <svg width="36" height="34" viewBox="0 0 36 34" fill="none" stroke="#12335a" stroke-width="2"><rect x="2" y="4" width="32" height="20"/><path d="M14 24l-2 6h12l-2-6" fill="#12335a"/></svg>
  <h4>Webdesign &amp; Entwicklung</h4>
  <p>Eine kompetente und detaillierte Planung Ihres Projektes beziehungsweise Webauftritts steht für uns an erster Stelle und ist ein unerlässlicher Dienstleistungsbestandteil.</p>
</div>
<div class="abs card active" style="left:235px;top:1304px">
  <svg width="34" height="34" viewBox="0 0 34 34" fill="none" stroke="#12335a" stroke-width="2"><circle cx="19" cy="17" r="10"/><circle cx="19" cy="17" r="5" fill="#12335a"/><circle cx="8" cy="11" r="4"/><path d="M4 22h6"/></svg>
  <h4>Content Management Systeme (CMS)</h4>
  <p>Die Erstellung Ihrer Webseite mit Hilfe eines Content-Man-agement-Systems, wie zum Beispiel Seitenwerk, ermöglicht Ihnen eine einfache und selbstständige Wartung Ihrer gesamten Webpräsenz auch ohne Programmierkennt-</p>
</div>
<div class="abs card" style="left:609px;top:1304px">
  <svg width="34" height="34" viewBox="0 0 34 34" fill="#12335a"><path d="M17 4l13 26h-7l-6-13-6 13H4z"/><rect x="12" y="20" width="10" height="3" fill="#36cc96"/></svg>
  <h4>Corporate Design</h4>
  <p>Mit unserer Erfahrung und der partnerschaftlichen Zusam-menarbeit erarbeiten wir eine maßgeschneiderte Lösung für Ihr Corporate Design. Wir ermöglichen Ihnen eine moderne Überarbeitung Ihres bestehenden Corporate</p>
</div>
<div class="abs card" style="left:235px;top:1448px">
  <div class="icon-t">T</div>
  <h4>Homepage Texte</h4>
  <p>Mit ansprechenden, anspruchsvollen und verständlichen Texten innerhalb Ihrer Webpräsenz erreichen Sie die volle Aufmerksamkeit Ihrer Kundinnen und Kunden.</p>
</div>
<div class="abs card" style="left:609px;top:1448px">
  <svg width="34" height="34" viewBox="0 0 34 34" fill="none" stroke="#12335a" stroke-width="2"><path d="M12 31v-6c-4-2-6-6-6-10a11 11 0 0 1 22 0l2 5h-3v5h-5v6"/><circle cx="17" cy="14" r="3"/><path d="M17 17l3 4"/></svg>
  <h4>Support &amp; Service</h4>
  <p>Hilfestellung, Unterstützung sowie fachmännischer Kun-dendienst rund um Ihre Webpräsenz nehmen für uns einen wichtigen Stellenwert ein.</p>
</div>
<a class="abs btn" href="#" style="left:529px;top:1618px;width:138px;height:36px;line-height:36px">KONTAKT AUFNEHMEN</a>

<!-- references -->
<h2 class="abs section-title" style="top:1745px">Referenzen<span>_</span></h2>
<p class="abs section-sub" style="top:1769px">Meine Referenzen sind der glaubhafte Beleg für den Erfolg meiner Dienstleistungen.</p>
<div class="abs divider"></div>
<div class="abs filters"><span class="on">Alle</span><span>Webdesign</span><span>Appdesign</span><span>Development</span></div>

<div class="abs tile" style="left:234px;top:1863px;width:365px;height:363px;background:linear-gradient(120deg,#2bc3a6 0%,#35c7ab 35%,#e9edf1 55%,#f05f56 80%,#f5f5f5 100%)" role="img" aria-label="Zwei Smartphones mit Profil-App, Referenz Appdesign"></div>
<div class="abs tile" style="left:599px;top:1863px;width:183px;height:181px;background:linear-gradient(135deg,#3f6d6b 0%,#2d4f52 50%,#6f8f8a 100%)" role="img" aria-label="Smartphones mit Chat-App auf grünem Hintergrund"></div>
<div class="abs tile" style="left:782px;top:1863px;width:183px;height:181px;background:#48617f" role="img" aria-label="Webdesign-Referenz Yacht Vermietung">
  <div class="yacht" style="width:183px;height:181px">
    <small>Webdesign</small>
    <strong>Yacht Vermietung</strong>
    <span>Lorem ipsum dolores set amet victim ante arcus.</span>
    <em>Read more</em>
  </div>
</div>
<div class="abs tile" style="left:599px;top:2044px;width:183px;height:182px;background:linear-gradient(180deg,#4a4b4c 0%,#2e2a28 55%,#6a5a3a 100%)" role="img" aria-label="Smartphone-Ansicht mit Foto einer Frau mit Blumenstrauss"></div>
<div class="abs tile" style="left:782px;top:2044px;width:183px;height:182px;background:linear-gradient(180deg,#f6f6f4 0%,#f1f1ee 50%,#dfe7ee 100%)" role="img" aria-label="Illustrierte Webseite Team Work mit Figuren und Werkzeugen"></div>

<a class="abs btn" href="#" style="left:543px;top:2269px;width:112px;height:35px;line-height:35px">ALLE ANSEHEN</a>

<!-- contact & footer -->
<footer class="abs footer" role="img" aria-label="Schreibtisch mit Tastatur und Notizbuch in Blau getönt"></footer>
<div class="abs stripe"></div>

<form class="abs form-card">
  <h3>Nehmen Sie Kontakt auf:</h3>
  <div class="field" style="left:41px;top:73px;width:162px"><label>vollständiger Name</label><span>Lina Hofer</span></div>
  <div class="field" style="left:232px;top:73px;width:163px"><label>Email Adresse</label><span>info@hoferstudio.com</span></div>
  <div class="field" style="left:41px;top:130px;width:162px"><label>Betreff</label><span>Lorem ipsum</span></div>
  <div class="field" style="left:41px;top:187px;width:354px"><label>Ihre Nachricht</label><span>Hallo! Etiam sit amet orci eget eros faucibus tincidunt. Beste Grüße, Lina</span></div>
  <a class="abs btn" href="#" style="left:266px;top:248px;width:138px;height:35px;line-height:35px">KONTAKT AUFNEHMEN</a>
</form>

<p class="abs foot-text" style="left:231px;top:2764px;width:250px">Etiam sit amet orci eget eros faucibus tincidunt. Duis leo. Sed fringilla mauris sit amet nibh. Etiam sit amet orci eget eros faucibus tincidunt Duis leo.</p>
<p class="abs foot-text" style="left:231px;top:2820px">© 2016 MASO &nbsp;- &nbsp;&nbsp;Alle Rechte vorbehalten</p>
<ul class="abs foot-list" style="left:558px;top:2761px"><li>STARTSEITE</li><li>ÜBER MICH</li><li>LEISTUNGEN</li><li>REFERENZEN</li></ul>
<ul class="abs foot-list" style="left:687px;top:2761px"><li>KONTAKT</li><li>DATENSCHUTZ</li><li>IMPRESSUM</li></ul>
<p class="abs foot-text" style="left:851px;top:2762px;font-size:10.5px;line-height:16px">Lindenweg 14<br>9000 St. Gallen</p>
<p class="abs foot-text" style="left:851px;top:2809px;font-size:10.5px;line-height:16px">030 / 48 15 92 07<br>hallo@masoweb.ch</p>

</body>
</html>
```